new letterhead for my brokergae company BoatCrest, Complete Marine Brokering

We need a new letterhead for our brokerage company called BoatCrest. We are specialised in selling pleasure crafts (sailing and motoryachts). More info can be found at https://boatcrest-example.com/en

I use this document for a quotation, a letter, sales agreement, selling instructions. I am looking for a cover page + a content page.

Th efollowing information needs to be in the header / footer; email, website, VAT number, Bank Account number, number chamber of ccomerce, registry number orvd, General terms and conditions KLTV apply.

```html
<!DOCTYPE html>
<html lang="en">
<head>
<meta charset="utf-8">
<title>BoatCrest – Cover and Letterhead</title>
<link rel="stylesheet" href="https://fonts.googleapis.com/css2?family=Jost:wght@300;400&family=Arimo:wght@400;700&display=swap">
<style>
  :root{
    --bg:#e4e4e4;
    --blue:#0e5aa2;
    --blue-deep:#0b4e8f;
    --blue-light:#5cb0dc;
    --sea:#1d4f80;
    --sea-dark:#1b2633;
    --grey:#8a8a8a;
    --grey-text:#b8b8b8;
    --paper:#f7f7f7;
    --ink:#333;
    --muted:#666;
  }
  *{margin:0;padding:0;box-sizing:border-box}
  html,body{width:1200px;height:901px;overflow:hidden;background:var(--bg)}
  .canvas{position:relative;width:1200px;height:901px}
  .sheet{position:absolute;top:105px;width:490px;height:692px;overflow:hidden}
  .cover{left:82px;background:var(--blue)}
  .letter{left:630px;background:var(--paper)}

  /* cover */
  .cover-stripe{position:absolute;left:358px;top:0;width:92px;height:692px;background:var(--blue-deep)}
  .cover-photo{position:absolute;left:0;top:368px;width:490px;height:222px;
    background:linear-gradient(180deg,#6f7f8f 0%,#2c3a48 35%,#d7dde3 55%,#1e5a8e 70%,#173f6a 100%)}
  .cover-photo-tint{position:absolute;left:358px;top:368px;width:92px;height:222px;background:var(--blue-light);opacity:.55}
  .cover-foot{position:absolute;left:0;top:590px;width:490px;height:102px;background:var(--grey)}
  .cover-foot-stripe{position:absolute;left:358px;top:590px;width:92px;height:102px;background:var(--blue)}
  .brand{position:absolute;font-family:"Jost",sans-serif;font-weight:400;line-height:1}
  .cover .brand{left:54px;top:72px;color:#fff}
  .brand-name{font-size:30px;display:block}
  .brand-tag{font-size:6.5px;letter-spacing:1.6px;text-transform:uppercase;display:block;margin-top:6px}
  .cover-title{position:absolute;left:46px;top:280px;font-family:"Jost",sans-serif;font-weight:300;line-height:1}
  .cover-title .kicker{display:block;color:#fff;font-size:25px}
  .cover-title .main{display:block;color:var(--grey-text);font-size:52px;letter-spacing:1px;margin-top:2px}
  .confidential{position:absolute;left:49px;top:644px;width:270px;border-top:1px solid #9c9c9c;padding-top:3px;
    font-family:"Arimo",sans-serif;font-size:4.6px;line-height:1.35;color:#a2a2a2}
  .confidential strong{display:block}

  /* letter */
  .letter .brand{left:38px;top:70px;color:var(--blue)}
  .letter .brand-name{font-size:22px}
  .letter .brand-tag{font-size:5px;letter-spacing:1.3px;margin-top:4px}
  .company-meta{position:absolute;right:38px;top:55px;text-align:right;font-family:"Arimo",sans-serif;font-size:6.3px;line-height:1.45;color:var(--muted)}
  .letter-body{position:absolute;left:38px;top:182px;width:414px;font-family:"Arimo",sans-serif;font-size:6.9px;line-height:1.27;color:var(--ink);text-align:justify}
  .letter-body p{margin-bottom:8px}
  .date{margin-bottom:10px!important}
  .recipient{margin-bottom:53px!important;text-align:left}
  .salutation{margin-bottom:6px!important}
  .closing{display:flex;align-items:flex-start;gap:18px;text-align:left;margin-top:14px}
  .signature{width:72px;height:36px;background:#e9ecf4;border-radius:3px}
  .letter-foot{position:absolute;left:0;bottom:0;width:490px;height:28px}
  .foot-address{position:absolute;left:38px;bottom:7px;font-family:"Arimo",sans-serif;font-size:6.3px;color:#fff}
  .foot-web{position:absolute;right:38px;bottom:17px;font-family:"Arimo",sans-serif;font-size:6.3px;letter-spacing:1.2px;color:var(--muted)}
  .foot-web b{color:var(--blue)}
</style>
</head>
<body>
<main class="canvas">

  <section class="sheet cover" aria-label="Proposal cover page">
    <div class="cover-stripe"></div>
    <div class="cover-photo" role="img" aria-label="Photo of a sailing yacht cruising on deep blue sea"></div>
    <div class="cover-photo-tint"></div>
    <div class="cover-foot"></div>
    <div class="cover-foot-stripe"></div>

    <div class="brand">
      <span class="brand-name">BoatCrest</span>
      <span class="brand-tag">Complete Marine Brokering</span>
    </div>

    <h1 class="cover-title">
      <span class="kicker">BUSINESS</span>
      <span class="main">PROPOSAL</span>
    </h1>

    <div class="confidential">
      <strong>Statement of Confidentiality</strong>
      This proposal and supporting materials contain confidential and proprietary business information of BoatCrest. These materials may be printed or photocopied for use in evaluating the proposed project, but are not to be shared with other parties.
    </div>
  </section>

  <section class="sheet letter" aria-label="Letter content page">
    <div class="brand">
      <span class="brand-name">BoatCrest</span>
      <span class="brand-tag">Complete Marine Brokering</span>
    </div>

    <div class="company-meta">
      VAT: 1234567<br>
      Bank Account number: 1234567<br>
      Registry number orvd: 1234567
    </div>

    <div class="letter-body">
      <p class="date">30.09.2017</p>
      <p class="recipient">Recipient's name<br>Lindenweg 4<br>10115 Berlin<br>Germany</p>
      <p class="salutation">Dear sir,</p>
      <p>Communication is a very integral part of living creatures, animals and humans. Communication may be verbal or written. Written communication however is only applicable to human beings. Can you even imagine a world without communication? Verbal communication can be through telephones, webcams or in person. Written communication is through letters, emails and mobile phone messages.</p>
      <p>In today's world of great inventions and technology, letters have somehow become redundant. It is the time for text messages or chats. But they still can communicate a lot more than all other modes of communication. Organizations and various government departments still bank on letters as a strong medium of communication. There is no comparison in costs of sending letters as compared to costs of mobile phone messages though – letters are far cheaper. Letters now commonly known as "hard copy documents" are considered more relevant and important than email copies of text messages as proof or evidence of some sort.</p>
      <p>Letters speak volumes about a person or an organization that writes it. So one must take utmost care ensuring that the language used in any letter is appropriate for the occasion for which it is being written. Since a letter is also a written proof or document, if there are certain things that should not form a part of it, then that too should be carefully handled.</p>
      <p>Writing a good letter is an art. But if for some reason someone is unable to write that perfect letter, these different types of letters provide a base for you to build on. Sample letters have been given for everyone to understand what all information needs to form a part of the letter type and then it can be customized.</p>
      <div class="closing">
        <p>Yours Sincerely,<br>Lena Vos</p>
        <div class="signature" role="img" aria-label="Handwritten signature"></div>
      </div>
    </div>

    <svg class="letter-foot" viewBox="0 0 490 28" aria-hidden="true">
      <polygon points="392,18 490,18 490,28 380,28" fill="#8e8e8e"/>
      <polygon points="300,12 400,12 392,18 290,28 280,28" fill="#c9c9c9"/>
      <polygon points="0,4 310,4 290,28 0,28" fill="var(--blue)"/>
      <polygon points="220,14 300,14 286,28 205,28" fill="var(--blue-deep)"/>
    </svg>
    <div class="foot-address">Havenkade 12, 4811 AB Breda · <b>T:</b> +31 00 000 00 00</div>
    <div class="foot-web">www.<b>boatcrest-example</b>.com</div>
  </section>

</main>
</body>
</html>
```